Need Powerpoint masters for my consulting company in privacy (RGPD) and IT

For my newly created consulting company I need powerpoint slides masters.
The company is specialzed in privacy (RGPD) and IT.
The company already has a logo (obtained via Marquelane).
These master slides will be mainly used when presenting reports/analysis to clients.
I'll attach a PNG files of the logo.

```html
<!DOCTYPE html>
<html lang="en">
<head>
<meta charset="utf-8">
<title>Lucien Farrand Conseil — Presentation Masters</title>
<link rel="stylesheet" href="https://fonts.googleapis.com/css2?family=Lato:wght@300;400;700&display=swap">
<style>
  :root{
    --navy:#05324c;
    --navy-deep:#031a2a;
    --night:#020b16;
    --teal:#0a8c9b;
    --teal-bright:#16a6b4;
    --teal-soft:#b5e0e4;
    --slate-soft:#a8bcc8;
    --grey:#a5a5a5;
    --grey-soft:#dcdcdc;
    --grid:#eeeeee;
    --ink:#1d2b36;
    --text-grey:#9a9a9a;
    --white:#ffffff;
    --sheet:#ffffff;
  }
  *{box-sizing:border-box;margin:0;padding:0}
  html,body{width:1200px;height:2206px;overflow:hidden;background:var(--sheet)}
  body{font-family:'Lato',sans-serif;color:var(--ink)}
  .deck{display:grid;grid-template-columns:536px 536px;grid-auto-rows:302px;gap:13px 14px;padding:6px 0 0 46px}
  .slide{position:relative;overflow:hidden;background:var(--white);box-shadow:0 2px 8px rgba(0,0,0,.08)}
  .photo{position:absolute;inset:0}
  .slide-title{position:absolute;left:27px;top:16px;font-size:18px;font-weight:400;color:var(--navy)}
  .slide-title::after{content:"";display:block;width:40px;height:1px;background:var(--teal);margin-top:8px}

  /* brand */
  .brand{display:flex;align-items:center;gap:5px;white-space:nowrap}
  .brand-mark{width:9px;height:9px;background:currentColor;flex:none}
  .brand-name{font-size:9px;font-weight:400;letter-spacing:.4px}
  .brand--light{color:var(--white)}
  .brand--footer{position:absolute;left:28px;top:270px;color:var(--navy)}
  .brand--footer .brand-mark{width:6px;height:6px}
  .brand--footer .brand-name{font-size:6.5px}

  /* footer */
  .footer-rule{position:absolute;left:0;right:10px;top:287px;height:1px;background:var(--teal-bright);opacity:.7}
  .copyright{position:absolute;right:38px;top:282px;font-size:4.5px;color:#666;background:var(--white);padding:0 3px}

  /* title blocks */
  .title-block{position:absolute;width:210px;display:flex;flex-direction:column;align-items:center;text-align:center;color:var(--white)}
  .rule{width:100%;height:1px;background:rgba(255,255,255,.45)}
  .pres-title{font-size:20px;font-weight:400;line-height:1.2;letter-spacing:.2px}
  .subtitle{font-size:11px;color:var(--teal-bright);letter-spacing:.2px}
  .website{position:absolute;font-size:6px;color:var(--white);display:flex;align-items:center;gap:8px}
  .website::after{content:"";width:20px;height:1px;background:rgba(255,255,255,.6)}

  /* title slides */
  .bg-circuit{background:radial-gradient(ellipse at 22% 35%,rgba(24,120,150,.55),transparent 55%),linear-gradient(115deg,#062338 0%,#041525 50%,#020a14 100%)}
  .bg-earth{background:radial-gradient(ellipse 60% 30% at 50% 105%,rgba(70,140,200,.55),transparent 70%),radial-gradient(ellipse at 50% 20%,#0a2036,transparent 70%),var(--night)}
  .bg-city{background:radial-gradient(ellipse at 35% 40%,rgba(60,80,95,.7),transparent 65%),linear-gradient(180deg,#202a35 0%,#141c25 60%,#0b1219 100%)}

  /* section dividers */
  .section-navy{background:var(--navy-deep)}
  .section-navy{background:#032a43}
  .section-teal{background:var(--teal)}
  .section-label{font-size:20px;font-weight:400;letter-spacing:.3px;margin-top:16px}

  /* agenda pills */
  .pill-list{position:absolute;left:29px;top:66px;width:485px;display:flex;flex-direction:column;gap:5px}
  .pill{position:relative;height:41px;display:flex}
  .pill-main{width:272px;height:100%;background:var(--navy);display:flex;align-items:center;padding-left:10px;gap:12px;color:var(--white)}
  .pill-side{flex:1;height:100%;background:var(--teal);border-radius:0 21px 21px 0;padding:8px 14px 0 16px;color:var(--white)}
  .pill-num{position:absolute;left:242px;top:6px;width:29px;height:29px;border-radius:50%;background:var(--white);border:2px solid var(--navy);color:var(--navy);font-size:14px;display:flex;align-items:center;justify-content:center}
  .mic{width:10px;height:12px;flex:none}
  .topic{font-size:10.5px;line-height:1.15}
  .topic small{display:block;font-size:6.5px}
  .topic small + small{font-size:5.2px;margin-top:1px}
  .side-label{font-size:6px}
  .side-text{font-size:6px;line-height:1.25}

  /* agenda grid */
  .agenda-grid{position:absolute;left:72px;top:82px;display:grid;grid-template-columns:218px 200px;row-gap:24px}
  .agenda-item{display:flex;gap:10px}
  .mic-badge{width:21px;height:21px;border-radius:50%;background:var(--teal);display:flex;align-items:center;justify-content:center;flex:none;margin-top:1px}
  .mic-badge .mic{width:8px;height:10px}
  .agenda-item h3{font-size:10.5px;font-weight:400;color:var(--ink)}
  .agenda-item .time{font-size:6px;color:var(--teal)}
  .agenda-item p{font-size:5.2px;color:var(--text-grey);line-height:1.3;width:152px}

  /* feature */
  .feature-photo{position:absolute;left:0;top:66px;width:268px;height:170px;background:radial-gradient(circle at 48% 40%,#9fe0ee 0%,#2b8ab0 18%,#0c4466 45%,#06213a 80%),#06213a}
  .feature-panel{position:absolute;left:268px;top:66px;width:268px;height:170px;background:var(--navy);color:var(--white);padding:26px 16px 0 27px}
  .feature-panel h2{font-size:14px;font-weight:400;margin-bottom:10px}
  .feature-panel p{font-size:7.6px;line-height:1.38;margin-bottom:8px}

  /* tile grid */
  .tile-grid{position:absolute;left:38px;top:67px;display:grid;grid-template-columns:repeat(3,149px);grid-template-rows:repeat(2,90px);gap:6px}
  .tile{padding:18px 10px 0 11px;color:var(--white)}
  .tile h3{font-size:8.5px;font-weight:400;margin-bottom:8px}
  .tile p{font-size:5.6px;line-height:1.3}
  .tile--teal{background:var(--teal)}
  .tile--navy{background:var(--navy)}
  .tile-city{background:linear-gradient(170deg,#2b3a4d 0%,#3d5a74 45%,#1a2a3b 100%)}
  .tile-globe{background:radial-gradient(circle at 50% 85%,#ffd9b0 0%,#4aa0c0 25%,#1d6f92 55%,#0d3c58 100%)}
  .tile-hands{background:linear-gradient(135deg,#f2ece6 0%,#e4cdbd 45%,#c79b84 75%,#f4f2ef 100%)}

  /* charts */
  .chart{position:absolute;top:68px;width:115px}
  .chart svg{display:block}
  .chart-caption{text-align:center;margin-top:8px}
  .chart-caption h3,.gauge-caption h3{font-size:9.5px;font-weight:700;letter-spacing:.2px}
  .chart-caption p,.gauge-caption p{font-size:5.3px;line-height:1.25;color:#444}
  .c-navy{color:var(--navy)} .c-teal{color:var(--teal)} .c-grey{color:var(--grey)}
  .c-grey h3{font-weight:400}
  .gauge{position:absolute;top:104px;width:100px;text-align:center}
  .gauge-caption{margin-top:8px}

  /* text slide */
  .text-body{position:absolute;left:27px;top:82px;width:480px}
  .text-lead{font-size:12.5px;line-height:1.3;color:var(--ink);margin-bottom:14px}
  .text-body p.copy{font-size:7.2px;line-height:1.4;color:var(--text-grey);margin-bottom:6px}

  .thanks{font-size:33px;font-weight:700;letter-spacing:.5px;margin-top:14px;white-space:nowrap}
</style>
</head>
<body>
<svg width="0" height="0" style="position:absolute" aria-hidden="true">
  <symbol id="mic" viewBox="0 0 10 12">
    <rect x="3.2" y="0.5" width="3.6" height="6.5" rx="1.8" fill="none" stroke="currentColor" stroke-width="1"/>
    <path d="M1.5 5.2a3.5 3.5 0 0 0 7 0" fill="none" stroke="currentColor" stroke-width="1"/>
    <path d="M5 8.7v2.5M3 11.3h4" stroke="currentColor" stroke-width="1"/>
  </symbol>
</svg>

<main class="deck">

  <!-- 1 Title: circuit -->
  <section class="slide">
    <div class="photo bg-circuit" role="img" aria-label="Dark blue technology background with glowing circuit lines"></div>
    <p class="website" style="right:0;top:29px">www.website.com</p>
    <div class="title-block" style="left:302px;top:106px">
      <div class="brand brand--light"><span class="brand-mark"></span><span class="brand-name">Lucien Farrand</span></div>
      <div class="rule" style="margin-top:20px"></div>
      <h1 class="pres-title" style="margin-top:14px">TITLE PRESENTATION<br>GOES HERE</h1>
      <div class="rule" style="margin-top:12px"></div>
      <p class="subtitle" style="margin-top:20px">SUBTITLE GOES HERE</p>
    </div>
  </section>

  <!-- 2 Title: earth -->
  <section class="slide">
    <div class="photo bg-earth" role="img" aria-label="Night view of planet Earth from space with a network glow"></div>
    <div class="title-block" style="left:163px;top:52px">
      <div class="brand brand--light"><span class="brand-mark"></span><span class="brand-name">Lucien Farrand</span></div>
      <h1 class="pres-title" style="margin-top:18px">TITLE PRESENTATION<br>GOES HERE</h1>
      <div class="rule" style="margin-top:8px"></div>
      <p class="subtitle" style="margin-top:7px">SUBTITLE GOES HERE</p>
      <div class="rule" style="margin-top:7px"></div>
    </div>
    <p class="website" style="left:239px;top:268px">www.website.com</p>
  </section>

  <!-- 3 Title: city -->
  <section class="slide">
    <div class="photo bg-city" role="img" aria-label="Dusk city skyline overlaid with faint security shield icons"></div>
    <p class="website" style="right:0;top:27px">www.website.com</p>
    <div class="title-block" style="left:275px;top:78px">
      <div class="brand brand--light"><span class="brand-mark"></span><span class="brand-name">Lucien Farrand</span></div>
      <h1 class="pres-title" style="margin-top:18px">TITLE PRESENTATION<br>GOES HERE</h1>
      <div class="rule" style="margin-top:8px"></div>
      <p class="subtitle" style="margin-top:7px;font-size:12px">SUBTITLE GOES HERE</p>
      <div class="rule" style="margin-top:7px"></div>
    </div>
  </section>

  <!-- 4 Agenda pills -->
  <section class="slide">
    <h2 class="slide-title">Our Agenda</h2>
    <div class="pill-list">
      <div class="pill">
        <div class="pill-main"><svg class="mic"><use href="#mic"/></svg><p class="topic">Your Topic Goes Here<small>10:00</small><small>Presented by: John Smith.</small></p></div>
        <div class="pill-side"><p class="side-label">Additional Info</p><p class="side-text">Lorem ipsum dolor sit amet, consectetur adipiscing elit, sed do eiusmod tempor labore.</p></div>
        <span class="pill-num">1</span>
      </div>
      <div class="pill">
        <div class="pill-main"><svg class="mic"><use href="#mic"/></svg><p class="topic">Your Topic Goes Here<small>10:00</small><small>Presented by: John Smith.</small></p></div>
        <div class="pill-side"><p class="side-label">Additional Info</p><p class="side-text">Lorem ipsum dolor sit amet, consectetur adipiscing elit, sed do eiusmod tempor labore.</p></div>
        <span class="pill-num">2</span>
      </div>
      <div class="pill">
        <div class="pill-main"><svg class="mic"><use href="#mic"/></svg><p class="topic">Your Topic Goes Here<small>10:00</small><small>Presented by: John Smith.</small></p></div>
        <div class="pill-side"><p class="side-label">Additional Info</p><p class="side-text">Lorem ipsum dolor sit amet, consectetur adipiscing elit, sed do eiusmod tempor labore.</p></div>
        <span class="pill-num">3</span>
      </div>
      <div class="pill">
        <div class="pill-main"><svg class="mic"><use href="#mic"/></svg><p class="topic">Your Topic Goes Here<small>10:00</small><small>Presented by: John Smith.</small></p></div>
        <div class="pill-side"><p class="side-label">Additional Info</p><p class="side-text">Lorem ipsum dolor sit amet, consectetur adipiscing elit, sed do eiusmod tempor labore.</p></div>
        <span class="pill-num">4</span>
      </div>
    </div>
    <div class="brand brand--footer"><span class="brand-mark"></span><span class="brand-name">Lucien Farrand</span></div>
    <div class="footer-rule"></div>
    <p class="copyright">© Copyright 2021 Lucien Farrand. All Right Reserved. &nbsp;|&nbsp; 4</p>
  </section>

  <!-- 5 Agenda grid -->
  <section class="slide">
    <h2 class="slide-title">Our Agenda</h2>
    <div class="agenda-grid">
      <div class="agenda-item"><span class="mic-badge"><svg class="mic" style="color:#fff"><use href="#mic"/></svg></span><div><h3>Agenda One</h3><p class="time">10:00</p><p>Lorem ipsum dolor sit amet, consectetur adipiscing elit, sed do eiusmod tempor labore.</p></div></div>
      <div class="agenda-item"><span class="mic-badge"><svg class="mic" style="color:#fff"><use href="#mic"/></svg></span><div><h3>Agenda Four</h3><p class="time">13:00</p><p>Lorem ipsum dolor sit amet, consectetur adipiscing elit, sed do eiusmod tempor labore.</p></div></div>
      <div class="agenda-item"><span class="mic-badge"><svg class="mic" style="color:#fff"><use href="#mic"/></svg></span><div><h3>Agenda Two</h3><p class="time">11:00</p><p>Lorem ipsum dolor sit amet, consectetur adipiscing elit, sed do eiusmod tempor labore.</p></div></div>
      <div class="agenda-item"><span class="mic-badge"><svg class="mic" style="color:#fff"><use href="#mic"/></svg></span><div><h3>Agenda Five</h3><p class="time">14:00</p><p>Lorem ipsum dolor sit amet, consectetur adipiscing elit, sed do eiusmod tempor labore.</p></div></div>
      <div class="agenda-item"><span class="mic-badge"><svg class="mic" style="color:#fff"><use href="#mic"/></svg></span><div><h3>Agenda Three</h3><p class="time">12:00</p><p>Lorem ipsum dolor sit amet, consectetur adipiscing elit, sed do eiusmod tempor labore.</p></div></div>
      <div class="agenda-item"><span class="mic-badge"><svg class="mic" style="color:#fff"><use href="#mic"/></svg></span><div><h3>Agenda Six</h3><p class="time">15:00</p><p>Lorem ipsum dolor sit amet, consectetur adipiscing elit, sed do eiusmod tempor labore.</p></div></div>
    </div>
    <div class="brand brand--footer"><span class="brand-mark"></span><span class="brand-name">Lucien Farrand</span></div>
    <div class="footer-rule"></div>
    <p class="copyright">© Copyright 2021 Lucien Farrand. All Right Reserved. &nbsp;|&nbsp; 5</p>
  </section>

  <!-- 6 Feature -->
  <section class="slide">
    <h2 class="slide-title">Title Goes Here</h2>
    <div class="feature-photo" role="img" aria-label="Glowing digital globe with network lines above a city skyline"></div>
    <div class="feature-panel">
      <h2>Heading Here</h2>
      <p>Lorem ipsum dolor sit amet, consectetur adipiscing elit, sed do eiusmod tempor incididunt ut labore et dolore magna aliqua. Ut enimad minim veniam, quis nostrud exercitation ullamco laboris nisi ut aliquip ex ea commodo consequat.</p>
      <p>Excepteur sint occaecat cupidatat non proident, sunt inculpa qui officia deserunt mollit anim id est laborum.</p>
    </div>
    <div class="brand brand--footer"><span class="brand-mark"></span><span class="brand-name">Lucien Farrand</span></div>
    <div class="footer-rule"></div>
    <p class="copyright">© Copyright 2021 Lucien Farrand. All Right Reserved. &nbsp;|&nbsp; 6</p>
  </section>

  <!-- 7 Section navy -->
  <section class="slide section-navy">
    <div class="title-block" style="left:277px;top:110px;width:210px">
      <div class="brand brand--light"><span class="brand-mark"></span><span class="brand-name">Lucien Farrand</span></div>
      <div class="rule" style="margin-top:13px"></div>
      <h2 class="section-label">SECTION DIVIDER</h2>
    </div>
  </section>

  <!-- 8 Section teal -->
  <section class="slide section-teal">
    <div class="title-block" style="left:277px;top:110px;width:210px">
      <div class="brand brand--light"><span class="brand-mark"></span><span class="brand-name">Lucien Farrand</span></div>
      <div class="rule" style="margin-top:13px"></div>
      <h2 class="section-label">SECTION DIVIDER</h2>
    </div>
  </section>

  <!-- 9 Tile grid -->
  <section class="slide">
    <h2 class="slide-title">Your Title Goes Here</h2>
    <div class="tile-grid">
      <div class="tile-city" role="img" aria-label="Night city skyline with security shield icons"></div>
      <div class="tile tile--teal"><h3>Heading Goes Here</h3><p>Lorem Ipsum dolor sit amer, consectetur adipiscing elit, sed do eiusmod tempor incididunt ut labore et commodo consequat dolore magna aliqua.</p></div>
      <div class="tile-globe" role="img" aria-label="Digital globe glowing over a city"></div>
      <div class="tile tile--navy"><h3>Heading Goes Here</h3><p>Lorem Ipsum dolor sit amer, consectetur adipiscing elit, sed do eiusmod tempor incididunt ut labore et commodo consequat dolore magna aliqua.</p></div>
      <div class="tile-hands" role="img" aria-label="Team joining hands together in a bright office"></div>
      <div class="tile tile--navy"><h3>Heading Goes Here</h3><p>Lorem Ipsum dolor sit amer, consectetur adipiscing elit, sed do eiusmod tempor incididunt ut labore et commodo consequat dolore magna aliqua.</p></div>
    </div>
    <div class="brand brand--footer"><span class="brand-mark"></span><span class="brand-name">Lucien Farrand</span></div>
    <div class="footer-rule"></div>
    <p class="copyright">© Copyright 2021 Lucien Farrand. All Right Reserved. &nbsp;|&nbsp; 9</p>
  </section>

  <!-- 10 Bar charts -->
  <section class="slide">
    <h2 class="slide-title">Our Chart #1</h2>

    <div class="chart c-navy" style="left:51px">
      <svg width="115" height="116" viewBox="0 0 115 116" font-family="Lato, sans-serif" font-size="4.5">
        <g stroke="var(--grid)" stroke-width=".8">
          <path d="M0 0H115M0 10H115M0 20H115M0 30H115M0 40H115M0 50H115M0 60H115M0 70H115M0 80H115M0 90H115M0 100H115"/>
          <path d="M16.4 0V108M32.8 0V108M49.2 0V108M65.6 0V108M82 0V108M98.4 0V108"/>
        </g>
        <g fill="var(--navy)">
          <rect x="1" y="54" width="15" height="54"/><rect x="17.4" y="68" width="15" height="40"/><rect x="33.8" y="55" width="15" height="53"/><rect x="50.2" y="30" width="15" height="78"/><rect x="66.6" y="73" width="15" height="35"/><rect x="83" y="54" width="15" height="54"/><rect x="99.4" y="97" width="15" height="11"/>
        </g>
        <g fill="#555" text-anchor="middle">
          <text x="8.5" y="51">50%</text><text x="25" y="65">37%</text><text x="41.3" y="52">49%</text><text x="57.7" y="27">72%</text><text x="74" y="70">32%</text><text x="90.5" y="51">50%</text><text x="107" y="94">10%</text>
          <text x="8.5" y="115">Sun</text><text x="25" y="115">Mon</text><text x="41.3" y="115">Tue</text><text x="57.7" y="115">Wed</text><text x="74" y="115">Thu</text><text x="90.5" y="115">Fri</text><text x="107" y="115">Sat</text>
        </g>
      </svg>
      <div class="chart-caption"><h3>INFODATA 01</h3><p>Lorem ipsum dolor sit amet,<br>consectetur adipiscing elit,<br>sed do eiusmod tempor</p></div>
    </div>

    <div class="chart c-teal" style="left:207px">
      <svg width="115" height="116" viewBox="0 0 115 116" font-family="Lato, sans-serif" font-size="4.5">
        <g stroke="var(--grid)" stroke-width=".8">
          <path d="M0 0H115M0 10H115M0 20H115M0 30H115M0 40H115M0 50H115M0 60H115M0 70H115M0 80H115M0 90H115M0 100H115"/>
          <path d="M16.4 0V108M32.8 0V108M49.2 0V108M65.6 0V108M82 0V108M98.4 0V108"/>
        </g>
        <g fill="var(--teal)">
          <rect x="1" y="73" width="15" height="35"/><rect x="17.4" y="48" width="15" height="60"/><rect x="33.8" y="12" width="15" height="96"/><rect x="50.2" y="63" width="15" height="45"/><rect x="66.6" y="92" width="15" height="16"/><rect x="83" y="53" width="15" height="55"/><rect x="99.4" y="83" width="15" height="25"/>
        </g>
        <g fill="#555" text-anchor="middle">
          <text x="8.5" y="70">32%</text><text x="25" y="45">56%</text><text x="41.3" y="9">89%</text><text x="57.7" y="60">42%</text><text x="74" y="89">15%</text><text x="90.5" y="50">51%</text><text x="107" y="80">23%</text>
          <text x="8.5" y="115">Sun</text><text x="25" y="115">Mon</text><text x="41.3" y="115">Tue</text><text x="57.7" y="115">Wed</text><text x="74" y="115">Thu</text><text x="90.5" y="115">Fri</text><text x="107" y="115">Sat</text>
        </g>
      </svg>
      <div class="chart-caption"><h3>INFODATA 02</h3><p>Lorem ipsum dolor sit amet,<br>consectetur adipiscing elit,<br>sed do eiusmod tempor</p></div>
    </div>

    <div class="chart c-grey" style="left:358px">
      <svg width="115" height="116" viewBox="0 0 115 116" font-family="Lato, sans-serif" font-size="4.5">
        <g stroke="var(--grid)" stroke-width=".8">
          <path d="M0 0H115M0 10H115M0 20H115M0 30H115M0 40H115M0 50H115M0 60H115M0 70H115M0 80H115M0 90H115M0 100H115"/>
          <path d="M16.4 0V108M32.8 0V108M49.2 0V108M65.6 0V108M82 0V108M98.4 0V108"/>
        </g>
        <g fill="var(--grey)">
          <rect x="1" y="61" width="15" height="47"/><rect x="17.4" y="94" width="15" height="14"/><rect x="33.8" y="38" width="15" height="70"/><rect x="50.2" y="77" width="15" height="31"/><rect x="66.6" y="70" width="15" height="38"/><rect x="83" y="24" width="15" height="84"/><rect x="99.4" y="46" width="15" height="62"/>
        </g>
        <g fill="#bbb" text-anchor="middle">
          <text x="8.5" y="58">44%</text><text x="25" y="91">13%</text><text x="41.3" y="35">65%</text><text x="57.7" y="74">29%</text><text x="74" y="67">35%</text><text x="90.5" y="21">78%</text><text x="107" y="43">57%</text>
          <text x="8.5" y="115" fill="#555">Sun</text><text x="25" y="115" fill="#555">Mon</text><text x="41.3" y="115" fill="#555">Tue</text><text x="57.7" y="115" fill="#555">Wed</text><text x="74" y="115" fill="#555">Thu</text><text x="90.5" y="115" fill="#555">Fri</text><text x="107" y="115" fill="#555">Sat</text>
        </g>
      </svg>
      <div class="chart-caption"><h3>INFODATA 03</h3><p>Lorem ipsum dolor sit amet,<br>consectetur adipiscing elit,<br>sed do eiusmod tempor</p></div>
    </div>

    <div class="brand brand--footer"><span class="brand-mark"></span><span class="brand-name">Lucien Farrand</span></div>
    <div class="footer-rule"></div>
    <p class="copyright">© Copyright 2021 Lucien Farrand. All Right Reserved. &nbsp;|&nbsp; 10</p>
  </section>

  <!-- 11 Gauges -->
  <section class="slide">
    <h2 class="slide-title">Our Chart #2</h2>
    <div class="gauge c-navy" style="left:44px">
      <svg width="100" height="54" viewBox="0 0 100 54" font-family="Lato, sans-serif">
        <path d="M8 50A42 42 0 0 1 92 50" fill="none" stroke="var(--slate-soft)" stroke-width="10"/>
        <path d="M8 50A42 42 0 0 1 92 50" fill="none" stroke="var(--navy)" stroke-width="10" pathLength="100" stroke-dasharray="15 100"/>
        <text x="50" y="43" text-anchor="middle" font-size="13" font-weight="700" fill="var(--navy)">15%</text>
      </svg>
      <div class="gauge-caption"><h3>INFODATA 01</h3><p>Lorem ipsum dolor sit amet,<br>consectetur adipiscing elit,<br>sed do eiusmod tempor</p></div>
    </div>
    <div class="gauge c-teal" style="left:158px">
      <svg width="100" height="54" viewBox="0 0 100 54" font-family="Lato, sans-serif">
        <path d="M8 50A42 42 0 0 1 92 50" fill="none" stroke="var(--teal-soft)" stroke-width="10"/>
        <path d="M8 50A42 42 0 0 1 92 50" fill="none" stroke="var(--teal)" stroke-width="10" pathLength="100" stroke-dasharray="47 100"/>
        <text x="50" y="43" text-anchor="middle" font-size="13" font-weight="700" fill="var(--teal)">47%</text>
      </svg>
      <div class="gauge-caption"><h3>INFODATA 02</h3><p>Lorem ipsum dolor sit amet,<br>consectetur adipiscing elit,<br>sed do eiusmod tempor</p></div>
    </div>
    <div class="gauge c-grey" style="left:272px">
      <svg width="100" height="54" viewBox="0 0 100 54" font-family="Lato, sans-serif">
        <path d="M8 50A42 42 0 0 1 92 50" fill="none" stroke="var(--grey-soft)" stroke-width="10"/>
        <path d="M8 50A42 42 0 0 1 92 50" fill="none" stroke="var(--grey)" stroke-width="10" pathLength="100" stroke-dasharray="60 100"/>
        <text x="50" y="43" text-anchor="middle" font-size="13" fill="var(--grey)">60%</text>
      </svg>
      <div class="gauge-caption"><h3>INFODATA 03</h3><p>Lorem ipsum dolor sit amet,<br>consectetur adipiscing elit,<br>sed do eiusmod tempor</p></div>
    </div>
    <div class="gauge c-navy" style="left:387px">
      <svg width="100" height="54" viewBox="0 0 100 54" font-family="Lato, sans-serif">
        <path d="M8 50A42 42 0 0 1 92 50" fill="none" stroke="var(--grey-soft)" stroke-width="10"/>
        <path d="M8 50A42 42 0 0 1 92 50" fill="none" stroke="var(--navy)" stroke-width="10" pathLength="100" stroke-dasharray="83 100"/>
        <text x="50" y="43" text-anchor="middle" font-size="13" font-weight="700" fill="var(--navy)">83%</text>
      </svg>
      <div class="gauge-caption"><h3>INFODATA 04</h3><p>Lorem ipsum dolor sit amet,<br>consectetur adipiscing elit,<br>sed do eiusmod tempor</p></div>
    </div>
    <div class="brand brand--footer"><span class="brand-mark"></span><span class="brand-name">Lucien Farrand</span></div>
    <div class="footer-rule"></div>
    <p class="copyright">© Copyright 2021 Lucien Farrand. All Right Reserved. &nbsp;|&nbsp; 11</p>
  </section>

  <!-- 12 Donuts -->
  <section class="slide">
    <h2 class="slide-title">Our Chart #3</h2>
    <svg class="donut-map" width="536" height="302" viewBox="0 0 536 302" style="position:absolute;inset:0" font-family="Lato, sans-serif">
      <defs>
        <filter id="soft-shadow" x="-30%" y="-30%" width="160%" height="160%"><feDropShadow dx="0" dy="2" stdDeviation="2.5" flood-color="#000" flood-opacity=".2"/></filter>
      </defs>
      <path d="M203 145Q270 200 333 145" fill="none" stroke="#8a98a3" stroke-width="1.2" stroke-dasharray="1.2 3"/>
      <g fill="var(--white)" stroke-width="1.4">
        <circle cx="203" cy="145" r="4.5" stroke="var(--grey)"/><circle cx="203" cy="145" r="1.6" fill="var(--grey)" stroke="none"/>
        <circle cx="333" cy="145" r="4.5" stroke="var(--teal)"/><circle cx="333" cy="145" r="1.6" fill="var(--teal)" stroke="none"/>
        <circle cx="270" cy="179" r="5" stroke="var(--navy)"/><circle cx="270" cy="179" r="1.8" fill="var(--navy)" stroke="none"/>
      </g>

      <circle cx="270" cy="102" r="49" fill="none" stroke="#e6e6e6" stroke-width="14"/>
      <circle cx="270" cy="102" r="49" fill="none" stroke="var(--navy)" stroke-width="14" pathLength="100" stroke-dasharray="87 100" transform="rotate(-90 270 102)"/>
      <text x="270" y="109" text-anchor="middle" font-size="18" font-weight="700" fill="var(--navy)">87%</text>

      <g filter="url(#soft-shadow)"><circle cx="162" cy="177" r="33" fill="#f2f2f2"/></g>
      <circle cx="162" cy="177" r="29" fill="none" stroke="#e2e2e2" stroke-width="8"/>
      <circle cx="162" cy="177" r="29" fill="none" stroke="#b5b5b5" stroke-width="8" pathLength="100" stroke-dasharray="15 100" transform="rotate(-90 162 177)"/>
      <circle cx="162" cy="177" r="22" fill="var(--white)"/>
      <text x="162" y="181" text-anchor="middle" font-size="10" fill="var(--grey)">15%</text>

      <g filter="url(#soft-shadow)"><circle cx="375" cy="177" r="33" fill="#f2f2f2"/></g>
      <circle cx="375" cy="177" r="29" fill="none" stroke="#e2e2e2" stroke-width="8"/>
      <circle cx="375" cy="177" r="29" fill="none" stroke="var(--teal)" stroke-width="8" pathLength="100" stroke-dasharray="32 100" transform="rotate(-90 375 177)"/>
      <circle cx="375" cy="177" r="22" fill="var(--white)"/>
      <text x="375" y="181" text-anchor="middle" font-size="10" font-weight="700" fill="var(--teal)">32%</text>

      <g filter="url(#soft-shadow)"><circle cx="270" cy="231" r="33" fill="#f2f2f2"/></g>
      <circle cx="270" cy="231" r="29" fill="none" stroke="#e2e2e2" stroke-width="8"/>
      <circle cx="270" cy="231" r="29" fill="none" stroke="var(--navy)" stroke-width="8" pathLength="100" stroke-dasharray="40 100" transform="rotate(-90 270 231)"/>
      <circle cx="270" cy="231" r="22" fill="var(--white)"/>
      <text x="270" y="235" text-anchor="middle" font-size="10" font-weight="700" fill="var(--navy)">40%</text>
    </svg>
    <div class="brand brand--footer"><span class="brand-mark"></span><span class="brand-name">Lucien Farrand</span></div>
    <div class="footer-rule"></div>
    <p class="copyright">© Copyright 2021 Lucien Farrand. All Right Reserved. &nbsp;|&nbsp; 12</p>
  </section>

  <!-- 13 Text -->
  <section class="slide">
    <h2 class="slide-title">Our Text Slide</h2>
    <div class="text-body">
      <p class="text-lead">This is place for your header text. Insert your text here, just replace this text with your own text</p>
      <p class="copy">Lorem ipsum dolor sit amet, consectetur adipiscing elit, sed do eiusmod tempor incididunt ut labore et dolore magna aliqua. Ut enimad minim veniam, quis nostrud exercitation ullamco laboris nisi ut aliquip ex ea commodo consequat.</p>
      <p class="copy">Duis aute irure dolor in reprehenderit in voluptate velit esse cillum dolore eu fugiat nulla pariatur. Ut enimad minim veniam, quis nostrud exercitation ullamco laboris nisi ut aliquip ex ea commodo consequat.<br>Excepteur sint occaecat cupidatat non proident, sunt inculpa qui officia deserunt mollit anim id est laborum.</p>
      <p class="copy">Ut enimad minim veniam, quis nostrud exercitation ullamco laboris nisi ut aliquip ex ea commodo consequat. Lorem ipsum dolor sit amet, consectetur adipiscing elit, sed do eiusmod tempor incididunt ut labore et dolore magna aliqua.</p>
    </div>
    <div class="brand brand--footer"><span class="brand-mark"></span><span class="brand-name">Lucien Farrand</span></div>
    <div class="footer-rule"></div>
    <p class="copyright">© Copyright 2021 Lucien Farrand. All Right Reserved. &nbsp;|&nbsp; 13</p>
  </section>

  <!-- 14 Thank you -->
  <section class="slide">
    <div class="photo bg-city" role="img" aria-label="Dusk city skyline overlaid with faint security shield icons"></div>
    <p class="website" style="right:0;top:27px">www.website.com</p>
    <div class="title-block" style="left:275px;top:118px">
      <div class="brand brand--light"><span class="brand-mark"></span><span class="brand-name">Lucien Farrand</span></div>
      <h2 class="thanks">THANK YOU</h2>
    </div>
  </section>

</main>
</body>
</html>
```